Stationary for I.T. company
DuskVale
Stationary for I.T. company - Information Technology
Creative Brief
Bright & Fun-filled
Ray Olsen
Director
PO Box 4172 Marlow ACT 2913
ops@duskva.le
duskva.le
Eye catching - display the DuskVale logo with either the red N with the white text or the white only logo on a background with either bold colours, dark greys or black. Open to other concepts or suggestions if they are eye catching
brimlow brimlow
Thank you everyone for your efforts. We may ask a couple more questons to relevant designers - but we plan to decide in the next 24 to 48 hours. Thanks again.
Thanks everyone for your submissions so far.. 266 designs is much much more than we were expecting. To help everyone understand where we are going and what we are looking for we will start eliminating some designs tonight. With that, we will probably start to give out a couple (maybe 3) 5 star ratings. These will indicate the current leading designs. We will probably also redo most of the star ratings out there to better give designers a better understanding of what we like. Please note that there is several people looking at these designs, so star rating may go up and down a little... but be assured if it has stars, we like it, or like some concepts in it.
We will aim to provide every designer feedback and stars (so yes - it may look like we rate a lot of things highly). 4 stars will generally be used to indicate the favorite submission of a designer, and 5 will only be used when we start eliminating designs.
tallfern tallfern
Check your private messages...
Also looking for letter head, invoice, envelope, notepad templates, presentation folder in addition to business card design. Thanks.
Amendment to the design brief - we will also accept a white background for the back of the business card

```html
<!DOCTYPE html>
<html lang="en">
<head>
<meta charset="utf-8">
<title>DuskVale business card</title>
<link href="https://fonts.googleapis.com/css2?family=Jost:wght@400;500;700&display=swap" rel="stylesheet">
<style>
  :root {
    --stage: #e9e7e4;
    --card-white: #ffffff;
    --card-black: #0b0b0c;
    --card-black-soft: #2a2a2c;
    --brand-red: #d81f26;
    --brand-red-dark: #9e1117;
    --ink: #4a4a4c;
    --ink-soft: #6e6e70;
  }
  * { margin: 0; padding: 0; box-sizing: border-box; }
  html, body {
    width: 1200px; height: 901px; overflow: hidden;
    background: var(--stage);
    font-family: "Jost", "Futura", sans-serif;
  }
  .canvas { position: relative; width: 1200px; height: 901px; }

  .card {
    position: absolute;
    width: 560px; height: 320px;
    border-radius: 18px;
    overflow: hidden;
    box-shadow: 0 10px 30px rgba(0,0,0,.18);
  }

  /* Back of card */
  .card-back {
    left: 90px; top: 90px;
    background: radial-gradient(ellipse at 40% 30%, var(--card-black-soft), var(--card-black) 70%);
    display: flex; align-items: center; justify-content: center; gap: 14px;
  }
  .card-back .brand-dot {
    width: 44px; height: 44px; border-radius: 50%;
    background: var(--brand-red);
  }
  .card-back .brand-name {
    color: #fff; font-weight: 500; font-size: 30px; letter-spacing: .5px;
  }

  /* Front of card */
  .card-front {
    left: 550px; top: 480px;
    background: var(--card-white);
  }
  .front-brand {
    position: absolute; left: 34px; top: 30px;
    display: flex; align-items: center; gap: 12px;
  }
  .front-brand .brand-dot {
    width: 40px; height: 40px; border-radius: 50%;
    background: var(--brand-red);
  }
  .front-brand .brand-name {
    color: var(--ink); font-weight: 500; font-size: 24px;
  }
  .contact {
    position: absolute; left: 34px; top: 102px;
    color: var(--ink-soft); font-size: 13px; line-height: 1.35;
  }
  .contact .person-name { color: var(--brand-red); font-size: 17px; font-weight: 500; }
  .contact .person-role { font-size: 12px; margin-bottom: 12px; }
  .contact .address { margin-bottom: 8px; }
  .contact-list { list-style: none; }
  .contact-list li { display: flex; align-items: center; gap: 8px; }
  .contact-list svg { width: 11px; height: 11px; fill: var(--brand-red); flex: none; }

  .hero-mark {
    position: absolute; right: -90px; top: 50px;
    width: 360px; height: 360px; border-radius: 50%;
    background: radial-gradient(circle at 35% 30%, var(--brand-red), var(--brand-red-dark));
  }
</style>
</head>
<body>
<main class="canvas">

  <section class="card card-back" aria-label="Card back">
    <span class="brand-dot"></span>
    <span class="brand-name">DuskVale</span>
  </section>

  <section class="card card-front" aria-label="Card front">
    <div class="front-brand">
      <span class="brand-dot"></span>
      <span class="brand-name">DuskVale</span>
    </div>

    <div class="contact">
      <p class="person-name">Ray Olsen</p>
      <p class="person-role">Director</p>
      <p class="address">PO Box 4172<br>Marlow ACT 2913</p>
      <ul class="contact-list">
        <li><svg viewBox="0 0 12 12"><path d="M2 1h3l1 3-2 1a7 7 0 0 0 3 3l1-2 3 1v3c-6 0-9-3-9-9z"/></svg>(02) 6200 3815</li>
        <li><svg viewBox="0 0 12 12"><path d="M3 0h6v12H3zM4 1v8h4V1z"/></svg>0412 557 308</li>
        <li><svg viewBox="0 0 12 12"><path d="M0 2h12v8H0zM1 3l5 4 5-4v-.5H1z"/></svg>ops@duskva.le</li>
        <li><svg viewBox="0 0 12 12"><circle cx="6" cy="6" r="5.5"/></svg>duskva.le</li>
      </ul>
    </div>

    <div class="hero-mark"></div>
  </section>

</main>
</body>
</html>
```